Website Front Page Banner Design for High Technology Intellectual Property

Develop Graphical Hero Banner to be used on the main page of Velmora .com. The banner will promote the availability of Velmora JESD204C IP (Intellectual Property). Please see attached pdf doc and follow details for Static Banner. We are looking for a Banner that is visually attention grabbing and uses imagery of applications that are enabled by the IP we are promoting (Applications such as 5G Wireless Infrastructure, CT/MRI/Ultrasound medical equipment, Radar / LIDAR / Satellites and High-Speed Test and Measurement equipment for a few examples). It would be good if the banner generally follow our color template of Green, White and Black - but the images of applications can use additional colors. Additonally, to learn more about JESD204 - recommend going to the following sites to understand what this IP is used for and what markets it address - additionally, I am open to answer any questions you may have. Sites: https://www.brantwise-labs.example/blog/high-speed-interface/jesd204c/, https://resources.quorvane.example/p/what-jesd204c-standard-adcs,
Target Market(s)
Various High Technology Markets such as Defense, Medical, Test and Measurement, Industrial / Robotics, Wireless Communications
Industry/Entity Type
Semiconductor

```html
<!DOCTYPE html>
<html lang="en">
<head>
<meta charset="utf-8">
<title>JESD204C IP Hero Banner</title>
<link href="https://fonts.googleapis.com/css2?family=Poppins:wght@400;500;600;700&display=swap" rel="stylesheet">
<style>
  :root {
    --stage: #3d3d3d;
    --navy: #1b3f60;
    --navy-deep: #163553;
    --teal: #1f6f78;
    --mint: #2fb58a;
    --green: #00b944;
    --white: #ffffff;
    --rule: #e3e3e3;
  }
  html, body {
    margin: 0;
    width: 1200px;
    height: 716px;
    overflow: hidden;
    background: var(--stage);
    font-family: "Poppins", sans-serif;
  }
  .hero {
    position: absolute;
    left: 128px;
    top: 125px;
    width: 924px;
    height: 462px;
    overflow: hidden;
    background: var(--navy);
  }
  .hero-visual {
    position: absolute;
    inset: 0;
    background:
      radial-gradient(ellipse 320px 240px at 740px 150px, rgba(47,181,138,0.75), transparent 70%),
      radial-gradient(ellipse 260px 200px at 850px 260px, rgba(47,181,138,0.55), transparent 70%),
      linear-gradient(90deg, var(--navy-deep) 0%, var(--navy) 38%, var(--teal) 70%, var(--mint) 100%);
  }
  .hero-edge {
    position: absolute;
    inset: 0;
    width: 924px;
    height: 462px;
  }
  .hero-copy {
    position: absolute;
    left: 54px;
    top: 68px;
    color: var(--white);
  }
  .eyebrow {
    margin: 0;
    color: var(--green);
    font-weight: 500;
    font-size: 30px;
    line-height: 34px;
    letter-spacing: -0.3px;
  }
  .headline {
    margin: 0;
    font-weight: 700;
    font-size: 47px;
    line-height: 46px;
    letter-spacing: -0.5px;
  }
  .lede {
    margin: 6px 0 0;
    font-size: 14.4px;
    line-height: 21.3px;
    width: 320px;
  }
  .features {
    list-style: none;
    margin: 12px 0 0 22px;
    padding: 0;
    font-size: 9.6px;
  }
  .features li {
    display: flex;
    align-items: center;
    gap: 7px;
    height: 21.3px;
  }
  .tick { width: 10px; height: 10px; flex: none; }
  .actions {
    display: flex;
    gap: 15px;
    margin-top: 15px;
  }
  .btn {
    display: flex;
    align-items: center;
    justify-content: center;
    height: 25px;
    border-radius: 2px;
    font-size: 9.2px;
    font-weight: 500;
  }
  .btn-primary { width: 119px; background: var(--green); color: var(--white); }
  .btn-secondary { width: 138px; background: var(--white); color: var(--green); font-weight: 400; letter-spacing: 0.3px; }
</style>
</head>
<body>
  <section class="hero">
    <div class="hero-visual" role="img" aria-label="Close-up photograph of a circuit board with a large processor chip and glowing green traces"></div>
    <svg class="hero-edge" viewBox="0 0 924 462" aria-hidden="true">
      <polygon points="0,462 924,378 924,462" fill="var(--rule)"/>
      <polygon points="0,462 924,386 924,462" fill="var(--white)"/>
      <polygon points="523,420 924,387 924,462" fill="var(--green)"/>
    </svg>
    <div class="hero-copy">
      <p class="eyebrow">JESD204C IP FOR</p>
      <h1 class="headline">EXTREME DATA<br>THROUGHPUT</h1>
      <p class="lede">High-speed ADC/DAC connectivity with deterministic latency and scalable multi-lane performance.</p>
      <ul class="features">
        <li><svg class="tick" viewBox="0 0 10 10"><circle cx="5" cy="5" r="4.2" fill="none" stroke="var(--green)" stroke-width="1"/><path d="M3 5.2 L4.5 6.6 L7.2 3.6" fill="none" stroke="var(--green)" stroke-width="1"/></svg>Up to 32 Gbps per Lane</li>
        <li><svg class="tick" viewBox="0 0 10 10"><circle cx="5" cy="5" r="4.2" fill="none" stroke="var(--green)" stroke-width="1"/><path d="M3 5.2 L4.5 6.6 L7.2 3.6" fill="none" stroke="var(--green)" stroke-width="1"/></svg>Deterministic Latency</li>
        <li><svg class="tick" viewBox="0 0 10 10"><circle cx="5" cy="5" r="4.2" fill="none" stroke="var(--green)" stroke-width="1"/><path d="M3 5.2 L4.5 6.6 L7.2 3.6" fill="none" stroke="var(--green)" stroke-width="1"/></svg>Scalable Multi-Lane Architecture</li>
        <li><svg class="tick" viewBox="0 0 10 10"><circle cx="5" cy="5" r="4.2" fill="none" stroke="var(--green)" stroke-width="1"/><path d="M3 5.2 L4.5 6.6 L7.2 3.6" fill="none" stroke="var(--green)" stroke-width="1"/></svg>Optimized for High-Performance FPGAs</li>
      </ul>
      <div class="actions">
        <span class="btn btn-primary">Explore JESD2046 IP</span>
        <span class="btn btn-secondary">Download Product Brief</span>
      </div>
    </div>
  </section>
</body>
</html>
```